Western Canadian Survey Company needs Business Card and Letter Head Design

Hello,

We're looking to have our business cards redesigned along with our letterhead.

We've recently changed out logo and would like to use this. Please use some creativity and propose different options (Traditional and modern).

We will provide as much feedback as possible.

Business card should be double sided with our logo. We would also like room for cell phone number, email address and position. Back of the card can just be our logo or potentially a list of our services we provide.

Industry/Entity Type

Business

Contact Information for Business Card

```html
<!DOCTYPE html>
<html lang="en">
<head>
<meta charset="utf-8">
<title>Ridgeline Field Surveys – Stationery</title>
<link href="https://fonts.googleapis.com/css2?family=Michroma&family=Raleway:wght@400;500&display=swap" rel="stylesheet">
<style>
:root{
  --backdrop:#d1d3d5;
  --paper:#ffffff;
  --ink:#111416;
  --slate:#567a8a;
  --slate-soft:#f2f3f5;
  --shadow:rgba(0,0,0,.45);
}
*{margin:0;padding:0;box-sizing:border-box}
html,body{width:1200px;height:918px;overflow:hidden;background:var(--backdrop)}
body{position:relative;font-family:"Raleway",sans-serif;color:var(--ink)}
.sheet{position:absolute;background:var(--paper);box-shadow:8px 8px 10px var(--shadow);overflow:hidden}
.letterhead{left:39px;top:48px;width:642px;height:831px}
.card{width:444px;height:253px}
.card-front{left:717px;top:202px}
.card-back{left:717px;top:472px;background:var(--slate);color:#fff}
.abs{position:absolute}
.brand-mark{font-family:"Michroma",sans-serif;font-weight:400;line-height:1;white-space:nowrap}
.company{font-family:"Michroma",sans-serif;color:var(--slate);line-height:1;white-space:nowrap;text-align:center}
.company .name{font-size:19px;letter-spacing:2px}
.company .sub{display:flex;align-items:center;gap:6px;font-size:7.5px;color:var(--ink);margin-top:2px;letter-spacing:.5px}
.company .sub::before,.company .sub::after{content:"";flex:1;height:1.5px;background:var(--ink)}
.card-back .company,.card-back .company .sub{color:#fff}
.card-back .company .sub::before,.card-back .company .sub::after{background:#fff}
.contact{font-size:12px;line-height:14.5px;white-space:nowrap}
.contact li{list-style:none;display:flex;align-items:center;gap:7px}
.contact svg{width:8px;height:8px;stroke:var(--slate);fill:none;stroke-width:1.3}
.rule{height:1.5px;background:var(--slate)}
.watermark{font-family:"Michroma",sans-serif;font-size:136px;color:var(--slate-soft);line-height:1;white-space:nowrap}
.divider{width:1.5px;background:var(--ink)}
.person-name{font-family:"Michroma",sans-serif;font-size:16.5px;color:var(--slate);white-space:nowrap}
.role{font-size:12px;text-transform:uppercase}
.services{font-size:11.5px;line-height:13.8px;text-align:center;list-style:none;width:100%}
</style>
</head>
<body>

<section class="sheet letterhead">
  <div class="abs brand-mark" style="left:104px;top:20px;font-size:31px">RFSL</div>
  <div class="abs company" style="left:27px;top:59px;width:272px">
    <div class="name">RIDGELINE FIELD</div>
    <div class="sub">SURVEYS LTD</div>
  </div>
  <ul class="abs contact" style="left:405px;top:58px">
    <li><svg viewBox="0 0 10 10"><path d="M2 1l2 2-1 1.5c.8 1.5 1.6 2.3 3 3L7.5 6l2 2-1.5 1.5C4.5 9 1 5.5.5 2.5z"/></svg>+330 555-0142</li>
    <li><svg viewBox="0 0 10 10"><rect x=".8" y="2" width="8.4" height="6"/><path d="M.8 2l4.2 3.3L9.2 2"/></svg>info@ridgelinefieldsurveys.com</li>
  </ul>
  <div class="abs rule" style="left:27px;top:97px;width:586px"></div>
  <div class="abs watermark" style="left:58px;top:338px">RFSL</div>
</section>

<section class="sheet card card-front">
  <div class="abs brand-mark" style="left:28px;top:108px;font-size:37px">RFSL</div>
  <div class="abs divider" style="left:192px;top:89px;height:74px"></div>
  <div class="abs person-name" style="left:207px;top:89px">MARCUS HALE</div>
  <div class="abs role" style="left:207px;top:109px">Director</div>
  <ul class="abs contact" style="left:207px;top:133px">
    <li><svg viewBox="0 0 10 10"><path d="M2 1l2 2-1 1.5c.8 1.5 1.6 2.3 3 3L7.5 6l2 2-1.5 1.5C4.5 9 1 5.5.5 2.5z"/></svg>+330 555-0142</li>
    <li><svg viewBox="0 0 10 10"><rect x=".8" y="2" width="8.4" height="6"/><path d="M.8 2l4.2 3.3L9.2 2"/></svg>info@ridgelinefieldsurveys.com</li>
  </ul>
</section>

<section class="sheet card card-back">
  <div class="abs brand-mark" style="left:0;width:444px;text-align:center;top:60px;font-size:31px;color:#fff">RFSL</div>
  <div class="abs company" style="left:81px;top:101px;width:282px">
    <div class="name">RIDGELINE FIELD</div>
    <div class="sub">SURVEYS LTD</div>
  </div>
  <ul class="abs services" style="left:0;top:143px">
    <li>QA/QC &amp; Survey Control</li>
    <li>Construction Surveys</li>
    <li>Underground Utility Location</li>
    <li>GIS / Drafting</li>
  </ul>
</section>

</body>
</html>
```